Label Design for Superfood product

Need a label for a green superfood product.
The name of the company is "Pelvo".
The product is a superfood powder made of several powerful ingredients that are all organic. The name of the products is Pelvo "Verdant Blend".
The label should be clean but still stand out. No pictures of fruit. The name of the company needs to be distinct and the main benefits.
Attached is a Sample of something we got with the general direction but it's not amazing.
Attached also variations of the logo (Several files).
Competitors are:
https://mytarlo.com/
http://brevix.com/
https://www.quendashop.com/

Industry/Entity Type

It Company

```html
<!DOCTYPE html>
<html lang="en">
<head>
<meta charset="utf-8">
<title>Pelvo Verdant Blend – Label</title>
<link href="https://fonts.googleapis.com/css2?family=Montserrat:wght@300;400;600;700;800&family=Archivo+Black&family=Arimo:wght@400;700&display=swap" rel="stylesheet">
<style>
  :root{
    --green-dark:#5d8a22;
    --green-mid:#6f9a2c;
    --green-light:#8cc63f;
    --green-wash:#e9f1dc;
    --ink:#222;
    --muted:#555;
    --white:#fff;
    --blue:#3b8fd6;
    --orange:#d9934a;
    --olive:#a8ad3a;
    --red:#d93a35;
    --icon-grey:#c9cbc6;
  }
  *{box-sizing:border-box;margin:0;padding:0}
  html,body{width:1059px;height:1200px;overflow:hidden;background:var(--white)}
  body{position:relative;font-family:"Arimo",Arial,sans-serif;color:var(--ink)}
  .label{
    position:absolute;left:0;top:495px;width:1059px;height:210px;
    background:linear-gradient(180deg,var(--green-dark) 0,var(--green-mid) 52px,var(--green-wash) 58px,#f7faf2 110px,var(--white) 150px);
  }
  .directions{position:absolute;left:19px;top:25px;width:265px;font-size:5.6px;line-height:7.4px;color:var(--white);font-family:"Montserrat",sans-serif;font-weight:400}
  .description{position:absolute;left:19px;top:65px;width:265px;font-size:5.6px;line-height:7.4px;color:var(--muted);font-family:"Montserrat",sans-serif}
  .warning{position:absolute;left:19px;top:112px;width:265px;font-size:5.6px;line-height:7.2px;font-weight:700;text-transform:uppercase;color:var(--ink)}
  .disclaimer{position:absolute;left:19px;top:137px;width:237px;border:1px solid #888;padding:2px 3px;font-size:5.4px;line-height:7px;color:var(--ink)}
  .badges{position:absolute;left:26px;top:172px;display:flex;gap:24px}
  .badge{width:20px;height:20px;border-radius:50%;border:1.5px solid var(--green-light);background:#f4f8ec}
  .badge.square{border-radius:3px;border-color:#2b4a9a;background:#e8ecf6}
  .badge.wide{width:36px;border-radius:3px;border-color:var(--green-dark)}

  .shield{position:absolute;left:428px;top:0;width:200px;height:142px}
  .brand{position:absolute;left:428px;top:14px;width:200px;text-align:center;font-family:"Montserrat",sans-serif;font-weight:800;font-size:30px;letter-spacing:0.5px;color:var(--white)}
  .product{position:absolute;left:428px;top:52px;width:200px;text-align:center;color:var(--white);font-family:"Montserrat",sans-serif;line-height:19px}
  .product .top{font-weight:700;font-size:19px;display:block}
  .product .bottom{font-weight:300;font-size:19px;display:block}
  .subtitle{position:absolute;left:428px;top:94px;width:200px;text-align:center;font-family:"Montserrat",sans-serif;font-weight:600;font-size:6.5px;color:var(--white)}
  .netwt{position:absolute;left:428px;top:111px;width:200px;text-align:center;font-family:"Montserrat",sans-serif;font-weight:700;font-size:8px;color:var(--white)}
  .macros{position:absolute;left:475px;top:146px;display:flex;gap:5px}
  .macro{width:23px;height:23px;border-radius:50%;display:flex;align-items:center;justify-content:center;color:var(--white);font-family:"Montserrat",sans-serif;font-weight:700;font-size:9px;border:1.5px solid rgba(255,255,255,.7);box-shadow:0 0 0 1px rgba(0,0,0,.08)}
  .macro.contains{background:var(--blue);font-size:4.5px;font-weight:600}
  .macro.carb{background:var(--orange)}
  .macro.protein{background:var(--olive)}
  .macro.fiber{background:var(--red)}
  .benefits{position:absolute;left:482px;top:173px;display:flex;gap:10px}
  .benefit{width:26px;text-align:center}
  .benefit-icon{width:20px;height:20px;margin:0 auto;border-radius:50%;background:var(--icon-grey);border:1px solid #aaa}
  .benefit-name{font-size:3.8px;font-family:"Montserrat",sans-serif;font-weight:600;margin-top:1px;text-transform:uppercase}

  .facts{position:absolute;left:872px;top:20px;width:161px;height:120px;background:var(--white);border:1.5px solid var(--green-light);padding:3px}
  .facts-inner{border:1px solid var(--ink);padding:2px 4px;height:100px}
  .facts-title{font-family:"Archivo Black",sans-serif;font-size:11px;line-height:12px}
  .facts-meta{font-size:4.8px;font-weight:700;line-height:6px}
  .facts-table{width:100%;border-collapse:collapse;font-size:4.6px;margin-top:2px}
  .facts-table th{text-align:right;border-top:3px solid var(--ink);border-bottom:1px solid var(--ink);padding:1px 0;font-weight:700}
  .facts-table td{border-bottom:0.5px solid #999;padding:0.6px 0;line-height:5.4px}
  .facts-table td.amt{text-align:right;padding-right:6px}
  .facts-table td.dv{text-align:right;width:8px}
  .facts-table tr:last-child td{border-bottom:2px solid var(--ink)}
  .facts-note{font-size:4.4px;margin-top:1px}
  .other{font-size:6.5px;margin-top:3px;padding-left:2px}
  .other b{font-weight:700}
  .maker{position:absolute;left:872px;top:172px;font-family:"Montserrat",sans-serif;font-size:7px;line-height:8px;color:var(--muted)}
  .maker b{color:var(--ink);font-weight:600}
</style>
</head>
<body>
<main class="label">
  <p class="directions">Add 1 serving (1 scoop) of Pelvo Verdant Blend one or two times everyday to 8-16 oz of ice-cold water or add it to your favorite rice milk, coconut milk, or almond milk and mix well. Pelvo's tip: Mix into your favorite smoothie.</p>
  <p class="description">Pelvo Verdant Blend provides 12 foods, herbs and nutrients in a single scoop of powder. This superfoods blend can help you feel better physically and mentally by improving healthy digestion, memory, and immunity. Nourish your body with nature's healthiest and best tasting superfoods in one drink. No preparation, no mess, no blending, no juicing. Simply mix in water and enjoy!</p>
  <p class="warning">Keep out of the reach of children. Do not use<br>if safety seal is damaged or missing.<br>Store in a cool, dry place.</p>
  <p class="disclaimer">* These statements have not been evaluated by the Food and Drug Administration.<br>This product is not intended to diagnose, treat, cure or prevent any disease.</p>
  <div class="badges">
    <span class="badge"></span>
    <span class="badge square"></span>
    <span class="badge wide"></span>
    <span class="badge"></span>
    <span class="badge"></span>
    <span class="badge"></span>
  </div>

  <svg class="shield" viewBox="0 0 200 142" aria-hidden="true">
    <defs>
      <linearGradient id="shieldFill" x1="0" y1="0" x2="0" y2="1">
        <stop offset="0" stop-color="#5d8a22"/>
        <stop offset="1" stop-color="#7aa832"/>
      </linearGradient>
    </defs>
    <path d="M2 0 H198 V68 Q198 104 100 140 Q2 104 2 68 Z" fill="#ffffff"/>
    <path d="M2 0 H198 V68 Q198 104 100 140 Q2 104 2 68 Z" fill="none" stroke="#8cc63f" stroke-width="3"/>
    <path d="M9 0 H191 V66 Q191 98 100 131 Q9 98 9 66 Z" fill="url(#shieldFill)"/>
  </svg>
  <div class="brand">PELVO</div>
  <div class="product"><span class="top">VERDANT</span><span class="bottom">BLEND</span></div>
  <div class="subtitle">DIETARY SUPPLEMENT</div>
  <div class="netwt">9.5 oz</div>
  <div class="macros">
    <span class="macro contains">Contains</span>
    <span class="macro carb">66g</span>
    <span class="macro protein">24g</span>
    <span class="macro fiber">87g</span>
  </div>
  <div class="benefits">
    <div class="benefit"><div class="benefit-icon" role="img" aria-label="Stomach icon for digestion"></div><div class="benefit-name">Digestion</div></div>
    <div class="benefit"><div class="benefit-icon" role="img" aria-label="Shield with cross icon for immunity"></div><div class="benefit-name">Immunity</div></div>
    <div class="benefit"><div class="benefit-icon" role="img" aria-label="Brain icon for function"></div><div class="benefit-name">Function</div></div>
  </div>

  <section class="facts">
    <div class="facts-inner">
      <div class="facts-title">Supplement Facts</div>
      <div class="facts-meta">Serving Size: 2 Scoops<br>Servings Per Container:</div>
      <table class="facts-table">
        <tr><th colspan="2">Amount Per Serving</th><th>%DV*</th></tr>
        <tr><td>Place Holder Ingredients</td><td class="amt">500 mg</td><td class="dv">†</td></tr>
        <tr><td></td><td class="amt">165 mg</td><td class="dv">†</td></tr>
        <tr><td></td><td class="amt">105 mg</td><td class="dv">†</td></tr>
        <tr><td></td><td class="amt">100 mg</td><td class="dv">†</td></tr>
        <tr><td></td><td class="amt">200 mcg</td><td class="dv">†</td></tr>
      </table>
      <div class="facts-note">† Daily Value (DV) not established</div>
    </div>
    <div class="other"><b>Other Ingredients:</b> Place Holder</div>
  </section>
  <div class="maker"><b>Manufactured for: PELVO</b><br>www.mypelvo.com<br>555-014-7720</div>
</main>
</body>
</html>
```